Business card for new business.
Red and black corporate colors.
Card can have an Indsutrial feel to it. Feel free to add Rust, Bolted steel, or graphics as you see fit. We provide highly specialized services to the below mentioned industries.
Keep information out of corners so that if I want I can choose rounded corners.
Information
- front. name - title - phone - email
- Rear
Pipelines - Transit - Construction - Quarrying - Power
Northgate - Ridgeford - Port Alder - Stonebrook - Westhaven

```html
<!DOCTYPE html>
<html lang="en">
<head>
<meta charset="UTF-8">
<title>Girderline Business Card</title>
<link href="https://fonts.googleapis.com/css2?family=Work+Sans:wght@400;500;800&display=swap" rel="stylesheet">
<style>
  :root {
    --bg: #1c1c1d;
    --card: #262627;
    --card-light: #323233;
    --red: #e3161c;
    --white: #ffffff;
    --soft: #e6e6e6;
  }
  * { box-sizing: border-box; margin: 0; padding: 0; }
  html, body {
    width: 1200px; height: 900px; overflow: hidden;
    background: var(--bg);
    font-family: "Work Sans", Arial, sans-serif;
  }
  .stage {
    width: 1200px; height: 900px;
    display: flex; flex-direction: column; align-items: center; justify-content: center;
    gap: 44px;
  }
  .card {
    position: relative;
    width: 672px; height: 384px;
    background: radial-gradient(circle at 75% 30%, var(--card-light), var(--card) 70%);
    border-bottom: 7px solid var(--red);
    box-shadow: 0 14px 30px rgba(0,0,0,.55);
    color: var(--white);
  }
  .wordmark {
    font-weight: 800;
    color: var(--white);
    letter-spacing: 1px;
    text-transform: uppercase;
    line-height: 1;
    white-space: nowrap;
  }
  /* Rear */
  .card--rear .wordmark {
    position: absolute; top: 112px; left: 0; right: 0;
    text-align: center; font-size: 62px;
  }
  .sectors {
    position: absolute; left: 0; right: 0; bottom: 38px;
    text-align: center; font-size: 16px; line-height: 1.45; color: var(--soft);
  }
  /* Front */
  .card--front .wordmark {
    position: absolute; top: 168px; left: 48px; width: 262px;
    text-align: center; font-size: 37px;
  }
  .divider {
    position: absolute; left: 340px; top: 104px; width: 2px; height: 170px;
    background: var(--soft);
  }
  .contact {
    position: absolute; left: 378px; top: 100px;
    font-size: 18px; line-height: 1.4; color: var(--soft);
  }
  .contact__name {
    color: var(--red); font-size: 27px; font-weight: 500; text-transform: uppercase; line-height: 1.1;
  }
  .contact__title { font-size: 18px; margin-bottom: 12px; }
  .contact__address { margin-bottom: 4px; }
  .contact__row { display: flex; align-items: center; gap: 10px; }
  .contact__row svg { width: 13px; height: 13px; flex: none; }
  .accent { color: var(--red); }
</style>
</head>
<body>
<main class="stage">
  <section class="card card--rear">
    <div class="wordmark">Girderline</div>
    <p class="sectors">
      Pipelines - Transit - Construction - Quarrying - Power<br>
      Northgate - Ridgeford - Port Alder - Stonebrook - Westhaven
    </p>
  </section>

  <section class="card card--front">
    <div class="wordmark">Girderline</div>
    <div class="divider"></div>
    <div class="contact">
      <div class="contact__name">Daniel Reyes</div>
      <div class="contact__title">Director</div>
      <div class="contact__address">2150 Ironwood Ave.<br>Austin, TX 78745</div>
      <div class="contact__row">
        <svg viewBox="0 0 24 24"><path fill="none" stroke="#e3161c" stroke-width="2.4" d="M5 3h4l2 5-2.5 1.5a12 12 0 0 0 6 6L16 13l5 2v4a2 2 0 0 1-2 2A17 17 0 0 1 3 5a2 2 0 0 1 2-2z"/></svg>
        <span>+330 5180-4417</span>
      </div>
      <div class="contact__row">
        <svg viewBox="0 0 24 24"><rect x="3" y="5" width="18" height="14" fill="none" stroke="#e3161c" stroke-width="2.4"/><path d="M3 6l9 7 9-7" fill="none" stroke="#e3161c" stroke-width="2.4"/></svg>
        <span>info@girderline.com</span>
      </div>
      <div class="contact__row">
        <svg viewBox="0 0 24 24"><circle cx="12" cy="12" r="9" fill="none" stroke="#e3161c" stroke-width="2.2"/><path d="M3 12h18M12 3c3 3 3 15 0 18M12 3c-3 3-3 15 0 18" fill="none" stroke="#e3161c" stroke-width="1.8"/></svg>
        <span>www.<span class="accent">girderline</span>.com</span>
      </div>
    </div>
  </section>
</main>
</body>
</html>
```